Brantley Water Taxi and Transport

Need to redesign our business cards to relay that we do freight logistics and water taxi service. We also work with gov. agencies doing environmental clean up, oil spill response, remote site construction and work with many of the air taxi and helicopter services on Kodiak Island. Out website is www.brantleywatertaxi-example.com to get a better idea of what we do.

Contact Information for Business Card

I have a previous business card but it just has the logo on the front, and a sunset picture on the back with the contact info. It does not relay what we do and what we can help with. I like a simple straight forward design over a busy one.

Colors
3176b5
0455a3
cfdfed

Requirements
Must have
• logo, email, website, phone number

```html
<!DOCTYPE html>
<html lang="en">
<head>
<meta charset="utf-8">
<title>Brantley Water Taxi and Transport – Business Cards</title>
<link href="https://fonts.googleapis.com/css2?family=Lato:wght@400;700;900&display=swap" rel="stylesheet">
<style>
  :root {
    --stage: #1c1c1c;
    --card: #121212;
    --blue-deep: #0455a3;
    --blue: #3176b5;
    --blue-light: #4aa8e0;
    --blue-pale: #cfdfed;
    --orange: #f39c12;
    --silver: #d6d6d6;
    --grey: #bdbdbd;
    --white: #ffffff;
  }
  * { box-sizing: border-box; margin: 0; padding: 0; }
  html, body { width: 1200px; height: 900px; overflow: hidden; }
  body {
    background: var(--stage);
    font-family: "Lato", Arial, sans-serif;
    position: relative;
  }
  .card {
    position: absolute;
    left: 340px;
    width: 520px;
    height: 300px;
    background: var(--card);
    border-radius: 22px;
    box-shadow: 0 18px 40px rgba(0,0,0,.55);
  }
  .card--back { top: 110px; }
  .card--front { top: 470px; }

  /* back */
  .back-brand {
    position: absolute;
    left: 0; right: 0; top: 96px;
    text-align: center;
    color: var(--silver);
  }
  .back-brand__name {
    font-weight: 900;
    font-size: 46px;
    letter-spacing: 3px;
    text-transform: uppercase;
    line-height: 1;
  }
  .back-brand__tag {
    font-size: 20px;
    margin-top: 6px;
  }
  .back-web {
    position: absolute;
    right: 60px; bottom: 46px;
    color: var(--white);
    font-size: 13px;
  }

  /* front */
  .front-brand {
    position: absolute;
    right: 36px; top: 70px;
    display: flex; align-items: center; gap: 12px;
    color: var(--blue);
  }
  .front-brand__mark {
    width: 22px; height: 22px; border-radius: 50%;
    background: var(--blue);
  }
  .front-brand__text { font-weight: 900; }
  .front-brand__name {
    font-size: 36px; letter-spacing: 2px; text-transform: uppercase; line-height: 1;
  }
  .front-brand__tag { font-size: 16px; margin-top: 4px; }
  .front-web {
    position: absolute;
    right: 36px; top: 170px;
    font-size: 14px;
    color: var(--blue-light);
  }
  .front-web .accent { color: var(--orange); }

  .person {
    position: absolute;
    left: 36px; bottom: 34px;
  }
  .person__name {
    color: var(--blue-deep);
    font-weight: 900;
    font-size: 22px;
    letter-spacing: .5px;
    text-transform: uppercase;
    line-height: 1;
  }
  .person__role {
    color: var(--grey);
    font-size: 15px;
    margin-top: 2px;
  }
  .contact { list-style: none; margin-top: 14px; }
  .contact__item {
    display: flex; align-items: center; gap: 7px;
    color: var(--white);
    font-size: 16px;
    line-height: 1.35;
  }
  .contact__icon { width: 14px; height: 14px; fill: var(--blue-deep); }
</style>
</head>
<body>
  <section class="card card--back" aria-label="Business card back">
    <div class="back-brand">
      <div class="back-brand__name">Brantley</div>
      <div class="back-brand__tag">Water Taxi &amp; Transport</div>
    </div>
    <div class="back-web">www.brantleywatertaxi-example.com</div>
  </section>

  <section class="card card--front" aria-label="Business card front">
    <div class="front-brand">
      <span class="front-brand__mark"></span>
      <div class="front-brand__text">
        <div class="front-brand__name">Brantley</div>
        <div class="front-brand__tag">Water Taxi &amp; Transport</div>
      </div>
    </div>
    <div class="front-web">www.<span class="accent">brantleywatertaxi-example</span>.com</div>

    <div class="person">
      <div class="person__name">Daniel Harper</div>
      <div class="person__role">Managing Director</div>
      <ul class="contact">
        <li class="contact__item">
          <svg class="contact__icon" viewBox="0 0 16 16" aria-hidden="true"><path d="M3 1h3l1.5 4-2 1.3a9 9 0 0 0 4.2 4.2L11 8.5l4 1.5v3a2 2 0 0 1-2 2A12 12 0 0 1 1 3a2 2 0 0 1 2-2z"/></svg>
          044-555 010 234
        </li>
        <li class="contact__item">
          <svg class="contact__icon" viewBox="0 0 16 16" aria-hidden="true"><path d="M1 3h14v10H1z M1 3l7 6 7-6" fill="var(--blue-deep)" stroke="var(--card)" stroke-width="1.2"/></svg>
          info@brantley-example.com
        </li>
      </ul>
    </div>
  </section>
</body>
</html>
```